New Business Card Design for Manufacturing

We are an engineering/manufacturing company that offers Advanced machining/assembly/engineering services, as well as innovative products for the heavy duty engine cooling markets.

We are looking to get a new business card designed that is clean and modern looking, but still fits the wide range of technical/skilled work we do.

- We hope to use this design as the base for other design work in new Presentations, web, and print work.

Industry/Entity Type

Engineering

Contact Information for Business Card

Our preferred color of blue is (RGB) 22/71/159 but can vary slightly from that color. Our content will be our Logo and full company name (Fabricated Tooling Works, Inc.), company address, name, job title, phone number with extension, cell number, fax number, website, and email address on the cards.
We'd like the full company name next to the logo, but we are open to other interpretations of that layout.
Preferably, we would like the back side to be clean with just our logo, and the front to contain all of the contact information.

Colors
2f74b4
0355a3
85abd2

Requirements
Must have
• - Logo, company name, needed content - We are open to interpretation beyond that.
• - Standard size business card.
• - Horizontal orientation.
• - Enough space for lengthy names / job titles (for example, a job title could read "Directory of Human Resources" or "V.P. of Governmental Affairs"). We need this to look clean, whether the title be short (CEO) or long (as described above).

```html
<!DOCTYPE html>
<html lang="en">
<head>
<meta charset="utf-8">
<title>Fabricated Tooling Works – Business Card</title>
<link href="https://fonts.googleapis.com/css2?family=Exo+2:wght@400;500;700;800;900&display=swap" rel="stylesheet">
<style>
  :root {
    --brand-blue: #1c479f;
    --ink: #222428;
    --card: #ffffff;
    --backdrop: #e9e6e1;
    --shadow: rgba(40, 30, 20, 0.18);
  }
  * { box-sizing: border-box; margin: 0; padding: 0; }
  html, body {
    width: 1200px; height: 800px; overflow: hidden;
    background: var(--backdrop);
    font-family: "Exo 2", "Segoe UI", sans-serif;
    color: var(--ink);
  }
  .canvas {
    position: relative; width: 1200px; height: 800px;
    display: flex; align-items: center; justify-content: center; gap: 60px;
  }
  .card {
    position: relative; width: 525px; height: 300px;
    background: var(--card);
    box-shadow: 0 10px 26px var(--shadow);
    overflow: hidden;
  }

  /* Back side */
  .card-back { display: flex; align-items: center; justify-content: center; }
  .brand-lockup { text-align: center; }
  .brand-name {
    font-weight: 900; font-size: 92px; line-height: 0.9;
    color: var(--brand-blue); letter-spacing: 2px;
  }
  .brand-tagline {
    margin-top: 10px; font-weight: 800; font-size: 25px;
    color: var(--ink); letter-spacing: 0.5px; text-transform: uppercase;
  }

  /* Front side */
  .contact-block { position: absolute; left: 34px; top: 30px; width: 300px; }
  .person {
    position: relative; padding-left: 20px;
  }
  .person::before {
    content: ""; position: absolute; left: 0; top: -2px;
    width: 6px; height: 46px; background: var(--brand-blue);
  }
  .person-name {
    font-weight: 700; font-size: 19px; color: var(--brand-blue);
    letter-spacing: 0.5px; text-transform: uppercase;
  }
  .person-title { font-size: 15.5px; margin-top: 1px; }

  .contact-list { list-style: none; margin-top: 20px; padding-left: 8px; }
  .contact-list li {
    display: flex; align-items: center; gap: 10px;
    font-size: 14.5px; line-height: 19px;
  }
  .contact-list .gap { margin-top: 12px; }
  .contact-list svg { width: 13px; height: 13px; fill: var(--brand-blue); flex: none; }

  .address { margin-top: 14px; padding-left: 0; font-size: 14.5px; line-height: 20px; }

  .side-brand {
    position: absolute; right: 30px; top: 20px; bottom: 20px;
    display: flex; align-items: center;
    writing-mode: vertical-rl; transform: rotate(180deg);
  }
  .side-brand-mark {
    font-weight: 900; font-size: 76px; line-height: 1;
    color: var(--brand-blue); letter-spacing: 2px;
  }
  .side-brand-company {
    font-weight: 700; font-size: 11.5px; line-height: 1;
    color: var(--ink); text-transform: uppercase; letter-spacing: 0.3px;
    margin-left: 6px;
  }
  .accent-bar {
    position: absolute; right: 0; bottom: 18px;
    width: 145px; height: 9px; background: var(--brand-blue);
  }
</style>
</head>
<body>
<main class="canvas">
  <section class="card card-back" aria-label="Card back">
    <div class="brand-lockup">
      <div class="brand-name">FTW</div>
      <div class="brand-tagline">Built for Tomorrow</div>
    </div>
  </section>

  <section class="card card-front" aria-label="Card front">
    <div class="contact-block">
      <div class="person">
        <h1 class="person-name">John Doe</h1>
        <p class="person-title">Directory of Human Resources</p>
      </div>
      <ul class="contact-list">
        <li><svg viewBox="0 0 16 16" aria-hidden="true"><path d="M4 0h8a1 1 0 0 1 1 1v14a1 1 0 0 1-1 1H4a1 1 0 0 1-1-1V1a1 1 0 0 1 1-1zm1 2v10h6V2zm3 11a1 1 0 1 0 0 2 1 1 0 0 0 0-2z"/></svg>123-456-7890</li>
        <li><svg viewBox="0 0 16 16" aria-hidden="true"><path d="M3.5 1 6 4 4.6 6.2a9 9 0 0 0 5.2 5.2L12 10l3 2.5-1.5 2.6C7.5 15 1 8.5.9 2.5z"/></svg>987-654-ABCD</li>
        <li><svg viewBox="0 0 16 16" aria-hidden="true"><path d="M4 1h7l2 2v3H4zM1 7h14v6h-2v2H3v-2H1zm4 3v4h6v-4z"/></svg>987-654-321</li>
        <li class="gap"><svg viewBox="0 0 16 16" aria-hidden="true"><path d="M0 3h16v1L8 9 0 4zm0 3 8 5 8-5v7H0z"/></svg>youremail@domain.com</li>
        <li><svg viewBox="0 0 16 16" aria-hidden="true"><path d="M8 0a8 8 0 1 0 0 16A8 8 0 0 0 8 0zm0 1.5c.8 0 1.8 1.8 2.1 5.2H5.9C6.2 3.3 7.2 1.5 8 1.5zM1.6 7.3h2.8c0 .5 0 1 .1 1.4H1.6a6.5 6.5 0 0 1 0-1.4zm4.3 0h4.2v1.4H5.9zm5.7 0h2.8a6.5 6.5 0 0 1 0 1.4h-2.9c.1-.4.1-.9.1-1.4zM5.9 9.3h4.2c-.3 3.4-1.3 5.2-2.1 5.2s-1.8-1.8-2.1-5.2z"/></svg>www.yoursite.com</li>
      </ul>
      <p class="address">418 Millbrook Road<br>Hadley, MA 01035</p>
    </div>

    <div class="side-brand">
      <span class="side-brand-mark">FTW</span>
      <span class="side-brand-company">Fabricated Tooling Works, Inc.</span>
    </div>
    <div class="accent-bar"></div>
  </section>
</main>
</body>
</html>
```